Redesign of key pages of website

We have a website in development: (You can see the test version here: https://staging.pawvira.ai) We want a redesign of a) the home page, b) the set up screens (all four steps), c) the account home page, and the chat page (all four linked below). It needs to look amazing in both desktop and mobile. Also, the chat page needs to have a few different versions to give people a choice between them.

Four areas:
1) Home page: https://staging.pawvira.ai/
2) Account pages: https://staging.pawvira.ai/account/chatsettings.php?step=1
3) Account home page (you'll need to set up an account which is free): https://staging.pawvira.ai/account/summary.php
4) Chat page: https://staging.pawvira.ai/chat.php?id=375

Also to clarify re: code, I don't need any of the interaction/behavior code. I just need the basic HTML and stylesheets so I can integrate that into the existing website.

Please feel free to pass by early versions to me or if you have any clarifications, let me know!

Industry/Entity Type

small businesses

Coding

Coded - Design and coding required

Number of Pages Required

5+ page

Font styles to use
Other font styles liked:
• keep the current font.

Requirements
Must have
• All the same elements/functionality on the current site. Just want a redesign. Also keep the dog visual. Also must work great in mobile and desktop and be really fun and modern and easy.
Nice to have
• Also in the setup pages, need a much better form of navigation (currently just have four circles.)

```html
<!DOCTYPE html>
<html lang="en">
<head>
<meta charset="utf-8">
<title>Pawvira – Chat</title>
<link href="https://fonts.googleapis.com/css2?family=Raleway:wght@400;500;600;800&family=Ubuntu:wght@400;500&display=swap" rel="stylesheet">
<style>
  :root{
    --page-bg:#f2f5fa;
    --card-bg:#ffffff;
    --sky:#cdecf8;
    --chat-bg:#f1f5fc;
    --ink:#1f2a3a;
    --ink-soft:#3d4a5c;
    --muted:#8a96ad;
    --tick:#7c8bb0;
    --accent:#3b8ef0;
    --accent-red:#ef5a5f;
    --line:#d9dee7;
    --navy:#2b3a5e;
    --dog-blue:#7aa0e8;
    --photo-warm:#b88563;
  }
  *{box-sizing:border-box;margin:0;padding:0}
  html,body{width:1200px;height:1074px;overflow:hidden}
  body{background:var(--page-bg);font-family:"Raleway",sans-serif;color:var(--ink);position:relative}

  .app-card{position:absolute;left:131px;top:100px;width:937px;height:830px;background:var(--card-bg);border-radius:31px;box-shadow:0 10px 30px rgba(40,60,100,.06)}

  .brand{position:absolute;left:164px;top:118px}
  .brand-name{font-family:"Raleway",sans-serif;font-weight:800;font-size:34px;color:var(--ink);letter-spacing:-.5px;line-height:1}
  .brand-tag{display:block;font-size:10.5px;color:var(--accent-red);margin-top:6px;margin-left:1px}

  .profile-card{position:absolute;left:144px;top:182px;width:237px;height:302px;background:var(--sky);border-radius:19px;text-align:center;box-shadow:0 12px 24px rgba(60,100,140,.08)}
  .profile-photo{position:absolute;left:55px;top:34px;width:128px;height:128px;border-radius:50%;border:1.5px solid #7cc3e0;background:radial-gradient(circle at 50% 40%,#e8c7ad,var(--photo-warm) 60%,#7a5038)}
  .profile-name{position:absolute;top:168px;width:100%;font-family:"Ubuntu",sans-serif;font-size:22px;font-weight:500;color:var(--ink)}
  .profile-role{position:absolute;top:194px;width:100%;font-family:"Ubuntu",sans-serif;font-size:12.5px;color:var(--ink-soft)}
  .profile-intro{position:absolute;top:218px;width:100%;font-size:11px;color:var(--ink)}
  .profile-social{position:absolute;top:248px;left:0;width:100%;display:flex;justify-content:center;gap:11px}
  .profile-social span{width:23px;height:23px;border-radius:50%;background:#1f5f7e}

  .side-nav{position:absolute;left:160px;top:528px;width:206px;list-style:none}
  .side-nav li{height:51px;border-bottom:1px solid var(--line);display:flex;align-items:center;justify-content:space-between;padding:0 6px 0 4px;font-size:15px;color:#4a5670;font-weight:500}
  .side-nav li:first-child{height:42px;align-items:flex-start}
  .side-nav svg{width:10px;height:14px}

  .chat-panel{position:absolute;left:394px;top:114px;width:661px;height:802px;background:var(--sky);border-radius:28px;overflow:hidden}
  .chat-header{height:68px;position:relative}
  .chat-avatar{position:absolute;left:24px;top:9px;width:46px;height:46px;border-radius:50%;border:2px solid #fff;background:radial-gradient(circle at 50% 40%,#e8c7ad,var(--photo-warm) 60%,#7a5038)}
  .chat-name{position:absolute;left:85px;top:13px;font-family:"Ubuntu",sans-serif;font-size:24px;color:var(--ink);line-height:1}
  .chat-role{position:absolute;left:85px;top:40px;font-family:"Ubuntu",sans-serif;font-size:12.5px;color:var(--ink-soft)}
  .chat-menu{position:absolute;right:22px;top:27px;width:22px;height:16px}
  .chat-body{position:absolute;left:0;top:68px;width:100%;height:734px;background:var(--chat-bg);border-radius:24px 24px 0 0}

  .scroll-track{position:absolute;left:647px;top:30px;width:4px;height:679px;background:#e3e8f1;border-radius:2px}
  .scroll-thumb{position:absolute;left:647px;top:68px;width:4px;height:81px;background:#c3cad8;border-radius:2px}

  .bubble{position:absolute;font-size:12.5px;line-height:19.4px;color:var(--ink);padding:0 19px;display:flex;align-items:center;border-radius:8px;font-weight:500}
  .bubble.out{background:var(--sky);border-radius:10px 10px 0 10px}
  .bubble.in{background:#fff;border-radius:10px 10px 10px 0}
  .stamp{position:absolute;font-size:11px;color:var(--tick);display:flex;align-items:center;gap:6px;font-weight:600}
  .stamp svg{width:17px;height:9px}
  .bot-avatar{position:absolute;left:26px;width:32px;height:32px;border-radius:50%;background:radial-gradient(circle at 40% 40%,#dfe8fb,var(--dog-blue))}
  .typing{position:absolute;left:73px;top:591px;width:50px;height:31px;background:#e3e6ec;border-radius:16px;display:flex;align-items:center;justify-content:center;gap:4px}
  .typing i{width:6px;height:6px;border-radius:50%;background:#6d7380}
  .typing i:last-child{width:4.5px;height:4.5px;background:#9aa0ab}

  .composer{position:absolute;left:28px;top:669px;width:534px;height:40px;background:#fff;border-radius:8px;font-size:12px;color:var(--muted);display:flex;align-items:center;padding-left:19px}
  .send-btn{position:absolute;left:576px;top:669px;width:43px;height:40px;background:var(--accent);border-radius:6px;display:flex;align-items:center;justify-content:center}

  .site-footer{position:absolute;left:0;top:976px;width:1200px;height:98px;background:var(--navy);color:#fff}
  .footer-nav{position:absolute;left:136px;top:39px;display:flex;gap:31px;font-size:16px;font-weight:600;list-style:none}
  .footer-nav li:nth-child(2){margin-right:7px}
  .footer-brand{position:absolute;left:474px;top:27px}
  .footer-brand .brand-name{color:#fff;font-size:32px}
  .footer-brand .brand-tag{margin-top:3px}
  .footer-social{position:absolute;left:806px;top:29px;display:flex;gap:10px}
  .footer-social span{width:30px;height:30px;border-radius:50%;border:1.5px solid #fff}
</style>
</head>
<body>
  <div class="app-card"></div>

  <div class="brand">
    <span class="brand-name">Pawvira</span>
    <span class="brand-tag">private beta</span>
  </div>

  <section class="profile-card">
    <div class="profile-photo" role="img" aria-label="Portrait photo of Nora, hair stylist"></div>
    <h2 class="profile-name">Nora</h2>
    <p class="profile-role">Hair Stylist</p>
    <p class="profile-intro">Talk to Vira, my AI assistant.</p>
    <div class="profile-social"><span></span><span></span></div>
  </section>

  <ul class="side-nav">
    <li>My Home Page<svg viewBox="0 0 10 14"><path d="M2 1l6 6-6 6" fill="none" stroke="#8a93a6" stroke-width="1.6"/></svg></li>
    <li>Demo Link<svg viewBox="0 0 10 14"><path d="M2 1l6 6-6 6" fill="none" stroke="#8a93a6" stroke-width="1.6"/></svg></li>
    <li>Demo Link<svg viewBox="0 0 10 14"><path d="M2 1l6 6-6 6" fill="none" stroke="#8a93a6" stroke-width="1.6"/></svg></li>
    <li>Demo Link<svg viewBox="0 0 10 14"><path d="M2 1l6 6-6 6" fill="none" stroke="#8a93a6" stroke-width="1.6"/></svg></li>
  </ul>

  <main class="chat-panel">
    <header class="chat-header">
      <div class="chat-avatar" role="img" aria-label="Small portrait photo of Nora"></div>
      <div class="chat-name">Nora</div>
      <div class="chat-role">Hair Stylist</div>
      <svg class="chat-menu" viewBox="0 0 22 16"><path d="M0 2h22M0 8h22M0 14h22" stroke="#1f2a3a" stroke-width="2.4"/></svg>
    </header>

    <div class="chat-body">
      <div class="scroll-track"></div><div class="scroll-thumb"></div>

      <div class="bubble out" style="left:382px;top:41px;width:237px;height:43px">Lorem Ipsum is simply dummy text</div>
      <div class="stamp" style="right:57px;top:88px"><svg viewBox="0 0 17 9"><path d="M1 5l3 3 6-7M7 8l7-7" fill="none" stroke="currentColor" stroke-width="1.4"/></svg>22:01</div>

      <div class="bubble out" style="left:73px;top:119px;width:546px;height:59px">Lorem Ipsum is simply dummy text of the printing and typesetting industry. Lorem Ipsum has been the industry’s standard dummy</div>
      <div class="stamp" style="right:57px;top:185px"><svg viewBox="0 0 17 9"><path d="M1 5l3 3 6-7M7 8l7-7" fill="none" stroke="currentColor" stroke-width="1.4"/></svg>22:01</div>

      <div class="bot-avatar" role="img" aria-label="Dog mascot avatar" style="top:219px"></div>
      <div class="bubble in" style="left:73px;top:210px;width:237px;height:44px">Lorem Ipsum is simply dummy text</div>
      <div class="stamp" style="left:242px;top:257px"><svg viewBox="0 0 17 9"><path d="M1 5l3 3 6-7M7 8l7-7" fill="none" stroke="currentColor" stroke-width="1.4"/></svg>22:01</div>

      <div class="bot-avatar" role="img" aria-label="Dog mascot avatar" style="top:341px"></div>
      <div class="bubble in" style="left:73px;top:293px;width:546px;height:83px">Lorem Ipsum is simply dummy text of the printing and typesetting industry. Lorem Ipsum has been the industry’s standard dummy when an unknown printer took a galley of type and scrambled it to make a type specimen book.</div>
      <div class="stamp" style="right:57px;top:385px"><svg viewBox="0 0 17 9"><path d="M1 5l3 3 6-7M7 8l7-7" fill="none" stroke="currentColor" stroke-width="1.4"/></svg>22:01</div>

      <div class="bubble out" style="left:73px;top:419px;width:546px;height:59px">Lorem Ipsum is simply dummy text of the printing and typesetting industry. Lorem Ipsum has been the industry’s standard dummy</div>
      <div class="stamp" style="right:57px;top:485px"><svg viewBox="0 0 17 9"><path d="M1 5l3 3 6-7M7 8l7-7" fill="none" stroke="currentColor" stroke-width="1.4"/></svg>22:01</div>

      <div class="bot-avatar" role="img" aria-label="Dog mascot avatar" style="top:519px"></div>
      <div class="bubble in" style="left:73px;top:510px;width:237px;height:44px">Lorem Ipsum is simply dummy text</div>
      <div class="stamp" style="left:242px;top:557px"><svg viewBox="0 0 17 9"><path d="M1 5l3 3 6-7M7 8l7-7" fill="none" stroke="currentColor" stroke-width="1.4"/></svg>22:01</div>

      <div class="typing"><i></i><i></i><i></i></div>

      <div class="composer">Messager ......</div>
      <div class="send-btn"><svg width="16" height="20" viewBox="0 0 16 20"><path d="M8 19V2M1 9l7-7 7 7" fill="none" stroke="#fff" stroke-width="2"/></svg></div>
    </div>
  </main>

  <footer class="site-footer">
    <ul class="footer-nav"><li>Home</li><li>Features</li><li>Demo</li></ul>
    <div class="footer-brand">
      <span class="brand-name">Pawvira</span>
      <span class="brand-tag">private beta</span>
    </div>
    <div class="footer-social"><span></span><span></span><span></span><span></span></div>
  </footer>
</body>
</html>
```